Business Card

I need a business card for my work as an energy lawyer. I am a single prctioner and I consult to energy companies regarding a variety of legal issues involving environmental matters, energy efficiency, regulations and contractual arrangements. i need a distinctive business card that stands out and is easy to read. I like bold colors or high contrast. I like a sparse architectural design. The font should be easy to read (many of my clients use reading glasses and are concerned about small type). The card should communicate that I am somewhat different from ordinary legal counsel. Below are some examples of cards that I like. Thank you for your interest and thought. Glen Dusty Harlow
Updates

Thanks to everyone who has submitted a design.  My general comments are:

1.  I like the colourful cards and the high contrast cards.
2.  I prefer the use of icons for home address, phone, mobile and email.
3.  For the high contrast cards please use three colours - black background, and red and white for the logo or information.
4.  The mobile number area code should be 403 and not 404.
5.  I also need to add a direct phone line which is 555-318-2967.

Thank you,

Glen Harlow

Project Deadline Extended
Reason: I have briefly extended the deadline by three days to allow those individuals who responded early to revise their designs based upon the subsequent clarification of the colours (red, white, black background) and the request to use icons and add a direct phone number.

Industry/Entity Type

Business

```html
<!DOCTYPE html>
<html lang="en">
<head>
<meta charset="utf-8">
<title>Glen Dusty Harlow — Business Card</title>
<link rel="stylesheet" href="https://fonts.googleapis.com/css2?family=Open+Sans:wght@400;600;700&display=swap">
<style>
  :root {
    --brand-blue: #0098dc;
    --ink: #333333;
    --paper: #ffffff;
    --stage-light: #ffffff;
    --stage-dark: #d2d2d2;
  }
  * { margin: 0; padding: 0; box-sizing: border-box; }
  html, body { width: 1200px; height: 849px; overflow: hidden; }
  body {
    position: relative;
    font-family: "Open Sans", Arial, sans-serif;
    background: radial-gradient(ellipse 60% 60% at 50% 48%, var(--stage-light) 0%, #ececec 55%, var(--stage-dark) 100%);
  }

  /* Front of card */
  .card-front {
    position: absolute;
    left: 101px; top: 91px;
    width: 520px; height: 301px;
    background: var(--paper);
    border: 8px solid var(--brand-blue);
  }
  .card-front .name {
    position: absolute; left: 38px; top: 40px;
    font-size: 16.5px; font-weight: 700; color: var(--brand-blue);
    letter-spacing: 0.2px; text-transform: uppercase;
  }
  .card-front .title {
    position: absolute; left: 39px; top: 63px;
    font-size: 13px; color: var(--ink);
  }
  .card-front .address {
    position: absolute; left: 39px; top: 91px;
    font-size: 13.5px; line-height: 19px; color: var(--ink); font-style: normal;
  }
  .contact-list {
    position: absolute; left: 39px; top: 196px;
    list-style: none; font-size: 13.5px; line-height: 18.5px; color: var(--ink);
  }
  .contact-list .label {
    display: inline-block; width: 54px;
    font-weight: 700; color: var(--brand-blue);
  }

  /* Back of card */
  .card-back {
    position: absolute;
    left: 573px; top: 465px;
    width: 530px; height: 303px;
    background: var(--brand-blue);
  }
  .signature-rule {
    position: absolute; left: 0; right: 0; top: 244px;
    display: flex; align-items: center; gap: 10px;
    color: var(--paper); text-transform: uppercase; font-weight: 700;
  }
  .signature-rule::before,
  .signature-rule::after {
    content: ""; height: 2px; background: var(--paper);
  }
  .signature-rule::before { width: 36px; }
  .signature-rule::after { flex: 1; }
  .signature-rule .first { font-size: 23px; }
  .signature-rule .rest { font-size: 16px; margin-left: 6px; }
</style>
</head>
<body>
  <section class="card-front" aria-label="Business card front">
    <h1 class="name">Glen Dusty Harlow</h1>
    <p class="title">Barrister and Solicitor, LLB, ICD.D</p>
    <address class="address">2718 Meadow Street S.W.<br>Calgary, Alberta</address>
    <ul class="contact-list">
      <li><span class="label">Phone</span>1.555.207.4183</li>
      <li><span class="label">Mobile</span>1.555.641.2039</li>
      <li><span class="label">Email</span>dusty@dustyharlow.com</li>
    </ul>
  </section>

  <section class="card-back" aria-label="Business card back">
    <div class="signature-rule"><span class="first">Glen</span><span class="rest">Dusty Harlow</span></div>
  </section>
</body>
</html>
```